Personal Training Elite Athletes

We are looking for a business card for elite athletic development business called Vanguard Peak. Our ultimate goal is to develop professional athletes. I would like to see the logo be a creative representation of the business name using Metallic Orange (including similar shades) and Silver. I would like the business card to communicate a modern, unique and sport feel.

Industry/Entity Type

Business

```html
<!DOCTYPE html>
<html lang="en">
<head>
<meta charset="utf-8">
<title>Vanguard Peak — Business Card</title>
<link rel="stylesheet" href="https://fonts.googleapis.com/css2?family=Exo+2:wght@400;500;600&display=swap">
<style>
  :root {
    --bg: #efefef;
    --card-black: #050505;
    --card-white: #f7f7f7;
    --orange: #f26a1b;
    --silver: #9a9a9a;
    --text-light: #f2f2f2;
    --text-grey: #8a8a8a;
  }
  * { box-sizing: border-box; margin: 0; padding: 0; }
  html, body { width: 1200px; height: 905px; overflow: hidden; }
  body {
    background: var(--bg);
    font-family: "Exo 2", sans-serif;
    position: relative;
  }
  .card {
    position: absolute;
    top: 304px;
    width: 520px;
    height: 297px;
    overflow: hidden;
    box-shadow: 0 6px 18px rgba(0,0,0,0.12);
  }
  .card--contact { left: 60px; display: flex; }
  .card--brand { left: 620px; background: var(--card-black); display: flex; align-items: center; justify-content: center; }

  .contact-panel {
    width: 50%;
    height: 100%;
    background: var(--card-black);
    position: relative;
    padding: 38px 0 0 36px;
    color: var(--text-light);
  }
  .accent-bar {
    position: absolute;
    left: 0; top: 0;
    width: 14px; height: 52px;
    background: var(--orange);
  }
  .person-name {
    color: var(--orange);
    font-size: 14px;
    font-weight: 500;
    letter-spacing: 0.06em;
    text-transform: uppercase;
  }
  .person-role {
    font-size: 13px;
    margin-top: 3px;
    margin-bottom: 34px;
  }
  .contact-list { list-style: none; font-size: 10.5px; line-height: 1; }
  .contact-list li { display: flex; align-items: center; gap: 7px; margin-bottom: 11px; }
  .contact-list svg { width: 11px; height: 11px; flex: none; fill: var(--orange); }
  .contact-address { font-size: 11.5px; margin-top: 6px; }

  .logo-panel {
    width: 50%;
    height: 100%;
    background: radial-gradient(circle at 50% 45%, #ffffff, var(--card-white) 70%, #e6e6e6);
    display: flex;
    align-items: center;
    justify-content: center;
  }
  .brand-lockup { display: flex; flex-direction: column; align-items: center; gap: 7px; }
  .brand-name {
    display: flex; align-items: center; gap: 8px;
    color: var(--orange);
    font-size: 22px;
    font-weight: 500;
    letter-spacing: 0.08em;
    text-transform: uppercase;
    white-space: nowrap;
  }
  .brand-mark { width: 14px; height: 14px; background: var(--orange); }
  .brand-tagline {
    color: var(--text-grey);
    font-size: 7.5px;
    letter-spacing: 0.14em;
    text-transform: uppercase;
    white-space: nowrap;
  }
  .card--brand .brand-name { font-size: 26px; }
  .card--brand .brand-mark { width: 16px; height: 16px; }
  .card--brand .brand-tagline { font-size: 8.5px; color: var(--silver); }
</style>
</head>
<body>
  <section class="card card--contact" aria-label="Contact side">
    <div class="contact-panel">
      <span class="accent-bar"></span>
      <p class="person-name">Daniel Whitmore</p>
      <p class="person-role">Managing Director</p>
      <ul class="contact-list">
        <li>
          <svg viewBox="0 0 24 24" aria-hidden="true"><path d="M6.6 10.8a15.1 15.1 0 0 0 6.6 6.6l2.2-2.2a1 1 0 0 1 1-.25 11.4 11.4 0 0 0 3.6.57 1 1 0 0 1 1 1V20a1 1 0 0 1-1 1A17 17 0 0 1 3 4a1 1 0 0 1 1-1h3.5a1 1 0 0 1 1 1c0 1.25.2 2.450.57 3.57a1 1 0 0 1-.25 1z"/></svg>
          014 552 3090
        </li>
        <li>
          <svg viewBox="0 0 24 24" aria-hidden="true"><path d="M6.6 10.8a15.1 15.1 0 0 0 6.6 6.6l2.2-2.2a1 1 0 0 1 1-.25 11.4 11.4 0 0 0 3.6.57 1 1 0 0 1 1 1V20a1 1 0 0 1-1 1A17 17 0 0 1 3 4a1 1 0 0 1 1-1h3.5a1 1 0 0 1 1 1c0 1.25.2 2.450.57 3.57a1 1 0 0 1-.25 1z"/></svg>
          014 552 3090
        </li>
        <li>
          <svg viewBox="0 0 24 24" aria-hidden="true"><path d="M2 5h20v14H2z M2 5l10 8 10-8" fill="none" stroke="#f26a1b" stroke-width="2.4"/></svg>
          hello@vanguardpeak.com
        </li>
        <li>
          <svg viewBox="0 0 24 24" aria-hidden="true"><circle cx="12" cy="12" r="9" fill="none" stroke="#f26a1b" stroke-width="2.4"/><path d="M3 12h18M12 3c3 3 3 15 0 18M12 3c-3 3-3 15 0 18" fill="none" stroke="#f26a1b" stroke-width="1.8"/></svg>
          vanguardpeak.com
        </li>
      </ul>
      <p class="contact-address">27 Harbour Street, Level 4, Eastgate</p>
    </div>
    <div class="logo-panel">
      <div class="brand-lockup">
        <p class="brand-name"><span class="brand-mark"></span>Vanguard Peak</p>
        <p class="brand-tagline">Train harder · Rise higher · Finish first</p>
      </div>
    </div>
  </section>

  <section class="card card--brand" aria-label="Brand side">
    <div class="brand-lockup">
      <p class="brand-name"><span class="brand-mark"></span>Vanguard Peak</p>
      <p class="brand-tagline">Train harder · Rise higher · Finish first</p>
    </div>
  </section>
</body>
</html>
```